Small but growing painting company. Have built up a steady client base. Want to start having a more professional look. Want to start with changing my business cards, and also getting new logo and tee shirts.

Target Market(s)

Home owners, property management companies, all ages 30-70

Industry/Entity Type

Painting And Decorating

Contact Information for Business Card

Bright Ridge Painting LLC Mark Delvecchi 630-584-3907 interior, exterior, vaulted ceiling, drywall repair, pressure washing, kitchen cabinets, epoxy, garage floors,

Font styles to use
Sans Serif
Other font styles liked:
• Harrington

Colors
0355a3
ffffff
ec1f27
000000
3176b5
0493ce
474747
b7b7b7

Requirements
Must have
• Creative, something that doesn’t look like every other painting card.
Nice to have
• I would like something with an arrow or something going to a point

```html
<!DOCTYPE html>
<html lang="en">
<head>
<meta charset="utf-8">
<title>Bright Ridge Painting LLC – Business Card</title>
<link href="https://fonts.googleapis.com/css2?family=Oswald:wght@400;500&family=Lato:wght@400&display=swap" rel="stylesheet">
<style>
  :root {
    --page-bg: #e6e6e6;
    --card-dark: #3d3c3e;
    --brand-red: #ec1f27;
    --circle-fill: #f1f0f0;
    --text-light: #ffffff;
    --text-dark: #303030;
  }
  html, body {
    margin: 0;
    width: 1200px;
    height: 900px;
    overflow: hidden;
    background: var(--page-bg);
  }
  .business-card {
    position: absolute;
    left: 110px;
    top: 147px;
    width: 980px;
    height: 606px;
    background: var(--card-dark);
    overflow: hidden;
    box-shadow: 0 10px 30px rgba(0,0,0,0.18);
  }
  .red-panel {
    position: absolute;
    right: 0;
    top: 0;
    width: 318px;
    height: 100%;
    background: var(--brand-red);
  }
  .brand-circle {
    position: absolute;
    left: 399px;
    top: 44px;
    width: 528px;
    height: 528px;
    border-radius: 50%;
    background: var(--circle-fill);
  }
  .brand-dot {
    position: absolute;
    left: 165px;
    top: 95px;
    width: 198px;
    height: 198px;
    border-radius: 50%;
    background: var(--brand-red);
  }
  .brand-name {
    position: absolute;
    left: 0;
    width: 100%;
    top: 336px;
    text-align: center;
    font-family: "Oswald", sans-serif;
    font-weight: 500;
    font-size: 38px;
    color: var(--text-dark);
    letter-spacing: 0.5px;
    margin: 0;
  }
  .owner-name {
    position: absolute;
    left: 45px;
    top: 64px;
    margin: 0;
    font-family: "Oswald", sans-serif;
    font-weight: 400;
    font-size: 40px;
    color: var(--brand-red);
    text-transform: uppercase;
    letter-spacing: 0.5px;
  }
  .contact-list, .service-list {
    position: absolute;
    left: 45px;
    margin: 0;
    padding: 0;
    list-style: none;
    font-family: "Lato", sans-serif;
    color: var(--text-light);
  }
  .contact-list {
    top: 140px;
    font-size: 27px;
    line-height: 35px;
  }
  .contact-list li {
    display: flex;
    align-items: center;
    gap: 8px;
  }
  .contact-icon {
    width: 22px;
    height: 22px;
    fill: var(--brand-red);
    flex: none;
  }
  .service-list {
    top: 335px;
    font-size: 28px;
    line-height: 35.6px;
  }
  .service-list li::before {
    content: "";
    display: inline-block;
    width: 10px;
    height: 10px;
    border-radius: 50%;
    background: var(--text-light);
    margin-right: 9px;
    vertical-align: middle;
    position: relative;
    top: -3px;
  }
</style>
</head>
<body>
  <div class="business-card">
    <div class="red-panel"></div>
    <div class="brand-circle">
      <div class="brand-dot"></div>
      <p class="brand-name">BRIGHT RIDGE PAINTING LLC</p>
    </div>

    <h1 class="owner-name">Mark Delvecchi</h1>

    <ul class="contact-list">
      <li>
        <svg class="contact-icon" viewBox="0 0 24 24" aria-hidden="true"><path d="M3 8c0-3 4-4 9-4s9 1 9 4v2h-5V8H8v2H3z M6 11h12l2 8H4z M12 13a2.5 2.5 0 1 0 0 5a2.5 2.5 0 1 0 0-5z"/></svg>
        630-584-3907
      </li>
      <li>
        <svg class="contact-icon" viewBox="0 0 24 24" aria-hidden="true"><path d="M2 5h20v14H2z M3.5 6.5 12 13l8.5-6.5z" fill-rule="evenodd"/></svg>
        hello@brightridgepaint.com
      </li>
      <li>
        <svg class="contact-icon" viewBox="0 0 24 24" aria-hidden="true"><circle cx="12" cy="12" r="10"/><path d="M7 8c2 0 3 1 3 3s2 2 2 4-1 3-1 5M14 4c0 2 2 2 3 3s2 2 4 2" stroke="#3d3c3e" stroke-width="1.6" fill="none"/></svg>
        www.brightridgepaint.com
      </li>
    </ul>

    <ul class="service-list">
      <li>Interior, Exterior</li>
      <li>Vaulted Ceiling</li>
      <li>Drywall Repair</li>
      <li>Pressure Washing</li>
      <li>Kitchen Cabinets</li>
      <li>Epoxy, Garage Floors.</li>
    </ul>
  </div>
</body>
</html>
```